Label design for Men's Coffee scrub

We need a label design for a coffee scrub.

The design should be black on white or white on black.
It will be a sticker label.
The bag is 15*23cm, you can design the label for 10.5*14.5cm
We are open to seeing one other feature colour used possibly for the flavour.

The product is designed primarily for men.
We'd like a clean appeal with some character.

The logo and the following text must be included on the label including a generated barcode.

INSERT LOGO

3 in 1 - PLAIN BODY CARE FOR HUMBLE FELLAS
Cleanses
Exfoliates
Moisturises

Targets Cellulite, stretch makes & unclogs pores

MILO’S Classic Grind Rub (flavour)

Directions: Get naked, get your skin wet, rub a modest amount of coffee scrub on your body in circular motions concentrating on problem areas. Rinse off. Patch test first if you have sensitive skin
Ingredients: Robusta Coffee Beans (Coffee), Prunus Amygdalus Dulcis (Sweet Almond Oil), Water (Aqua), Sodium Chloride (Himalyan Pink Salt), Sucrose (Brown Sugar), Simmondsia chinensis (Jojoba Oil), Origanum majorana (marjoram oil), Tocopheryl Acetate (Vitamin E), Fragrance (Parfum)*
*=natural

Australian Owned. Not tested on animals. ALL Natural

www.miloandthegrindrub.example
fb:/miloandthegrindrub
intsa: #milosgrindrub #humblefellasden #ruggedladsandgroundrub

Milo and the grind rub
PO BOX TBA
Melbourne, VIc
Australia 3000

Target Market(s)

Male 20's - late 40's

Requirements
Must have
• All text on one side
Nice to have
• be simple, clean, easy to read, refreshing. A small generated barcode
Should not have
• Any quirky images

```html
<!DOCTYPE html>
<html lang="en">
<head>
<meta charset="utf-8">
<title>Milo and the Grind Rub – Labels</title>
<link rel="stylesheet" href="https://fonts.googleapis.com/css2?family=Arvo:wght@400;700&family=Arimo:wght@400&display=swap">
<style>
  :root {
    --ink: #111111;
    --paper: #ffffff;
    --backdrop: #ecebe8;
  }
  * { box-sizing: border-box; margin: 0; padding: 0; }
  html, body {
    width: 1200px; height: 1000px; overflow: hidden;
    background: var(--backdrop);
  }
  .canvas {
    position: relative; width: 1200px; height: 1000px;
    display: flex; justify-content: center; align-items: center; gap: 70px;
  }
  .label {
    position: relative; width: 480px; height: 663px;
    padding: 12px;
    font-family: "Arvo", Georgia, serif;
  }
  .label--light { background: var(--paper); color: var(--ink); box-shadow: 0 2px 8px rgba(0,0,0,.12); }
  .label--dark  { background: var(--ink); color: var(--paper); }
  .label__frame {
    position: relative; height: 100%;
    border: 4px solid currentColor;
    padding: 34px 30px 20px;
    text-align: center;
  }
  .brand {
    display: flex; align-items: center; justify-content: center; gap: 10px;
    margin: 118px 0 40px;
    font-family: "Arvo", Georgia, serif;
    font-weight: 700; font-size: 26px; line-height: 1; letter-spacing: 1px;
  }
  .brand__mark { width: 14px; height: 14px; border-radius: 50%; background: currentColor; flex: none; }
  .claim {
    font-family: "Arimo", Arial, sans-serif;
    font-size: 13.5px; letter-spacing: .3px;
  }
  .benefits {
    font-family: "Arimo", Arial, sans-serif;
    font-size: 13px; margin-top: 3px; word-spacing: 4px;
  }
  .targets {
    font-family: "Arimo", Arial, sans-serif;
    font-size: 11.5px; margin-top: 16px;
  }
  .flavour { font-weight: 700; font-size: 16px; margin-top: 20px; }
  .section-title { font-weight: 400; font-size: 12.5px; letter-spacing: 2.5px; margin-top: 14px; }
  .directions { font-size: 10.2px; line-height: 1.3; }
  .ingredients { font-size: 7.6px; line-height: 1.35; margin-top: 1px; }
  .assurances { font-size: 8.2px; margin-top: 14px; }
  .web { font-weight: 700; font-size: 12px; margin-top: 14px; letter-spacing: .4px; }
  .social { font-size: 8.2px; margin-top: 4px; display: flex; flex-direction: column; align-items: center; gap: 3px; }
  .social__item { display: flex; align-items: center; gap: 5px; }
  .social__dot { width: 9px; height: 9px; border-radius: 50%; background: currentColor; }
  .address {
    position: absolute; left: 18px; bottom: 38px;
    font-style: normal; font-size: 7px; line-height: 1.3; text-align: left;
  }
  .barcode-area {
    position: absolute; left: 120px; bottom: 16px;
    width: 76px; height: 20px;
    border: 1px solid currentColor;
  }
  .weight {
    position: absolute; right: 20px; bottom: 14px;
    font-weight: 700; font-size: 24px;
  }
</style>
</head>
<body>
<main class="canvas">

  <article class="label label--light">
    <div class="label__frame">
      <h1 class="brand"><span class="brand__mark"></span>MILO AND THE GRIND RUB</h1>
      <p class="claim">3 in 1 - PLAIN BODY CARE FOR HUMBLE FELLAS</p>
      <p class="benefits">Cleanses - Exfoliantes - Moisturises</p>
      <p class="targets">Targets Cellulite, stretch makes &amp; unclogs pores</p>
      <h2 class="flavour">MILO’S Classic Grind Rub</h2>
      <h3 class="section-title">DIRECTIONS:</h3>
      <p class="directions">Get naked, get your skin wet, rub a modest amount of coffee scrub on your body in circular motions concentrating on problem areas. Rinse off. Patch test first if you have sensitive skin.</p>
      <h3 class="section-title">INGREDIENTS:</h3>
      <p class="ingredients">Robusta Coffee Beans (Coffee), Prunus Amygdalus Dulcis (Sweet Almond Oil), Water (Aqua), Sodium Chloride (Himalyan Pink Salt), Sucrose (Brown Sugar), Simmondsia chinensis (Jojoba Oil), Origanum majorana (marjoram oil), Tocopheryl Acetate (Vitamin E), Fragance (Parfum)* *=natural</p>
      <p class="assurances">Australian Owned. Not tested on animals. ALL Natural</p>
      <p class="web">www.miloandthegrindrub.example</p>
      <div class="social">
        <span class="social__item"><span class="social__dot"></span>:/miloandthegrindrub</span>
        <span class="social__item"><span class="social__dot"></span>#milosgrindrub</span>
      </div>
      <address class="address">Milo and the grind rub<br>PO BOX TBA<br>Melbourne, Vic<br>Australia 3000</address>
      <span class="barcode-area" role="img" aria-label="Barcode area"></span>
      <span class="weight">200g</span>
    </div>
  </article>

  <article class="label label--dark">
    <div class="label__frame">
      <h1 class="brand"><span class="brand__mark"></span>MILO AND THE GRIND RUB</h1>
      <p class="claim">3 in 1 - PLAIN BODY CARE FOR HUMBLE FELLAS</p>
      <p class="benefits">Cleanses - Exfoliantes - Moisturises</p>
      <p class="targets">Targets Cellulite, stretch makes &amp; unclogs pores</p>
      <h2 class="flavour">MILO’S Classic Grind Rub</h2>
      <h3 class="section-title">DIRECTIONS:</h3>
      <p class="directions">Get naked, get your skin wet, rub a modest amount of coffee scrub on your body in circular motions concentrating on problem areas. Rinse off. Patch test first if you have sensitive skin.</p>
      <h3 class="section-title">INGREDIENTS:</h3>
      <p class="ingredients">Robusta Coffee Beans (Coffee), Prunus Amygdalus Dulcis (Sweet Almond Oil), Water (Aqua), Sodium Chloride (Himalyan Pink Salt), Sucrose (Brown Sugar), Simmondsia chinensis (Jojoba Oil), Origanum majorana (marjoram oil), Tocopheryl Acetate (Vitamin E), Fragance (Parfum)* *=natural</p>
      <p class="assurances">Australian Owned. Not tested on animals. ALL Natural</p>
      <p class="web">www.miloandthegrindrub.example</p>
      <div class="social">
        <span class="social__item"><span class="social__dot"></span>:/miloandthegrindrub</span>
        <span class="social__item"><span class="social__dot"></span>#milosgrindrub</span>
      </div>
      <address class="address">Milo and the grind rub<br>PO BOX TBA<br>Melbourne, Vic<br>Australia 3000</address>
      <span class="barcode-area" role="img" aria-label="Barcode area"></span>
      <span class="weight">200g</span>
    </div>
  </article>

</main>
</body>
</html>
```